Business Card for Academic Coach

I need a business card designed for me - a private tutor/academic coach.

Glen Mabery
Academic Coach
AB Pellwood University, 1994 Cum Laude
Phone: 404-555-0187
glenrmabery@tutormail-example.com

Subjects
QET and BRT
Math, Physics, Writing

```html
<!DOCTYPE html>
<html lang="en">
<head>
<meta charset="utf-8">
<title>Glen Mabery – Academic Coach Business Card</title>
<link href="https://fonts.googleapis.com/css2?family=Arimo:wght@400&display=swap" rel="stylesheet">
<style>
  :root {
    --page-bg: #ebebeb;
    --blue-deep: #0052a3;
    --blue-mid: #005fb2;
    --blue-light: #0a80cc;
    --band-black: #000000;
    --rule-light: #c9dcef;
    --text-white: #ffffff;
  }
  * { margin: 0; padding: 0; box-sizing: border-box; }
  html, body {
    width: 1200px;
    height: 1000px;
    overflow: hidden;
    background: var(--page-bg);
    font-family: "Arimo", Arial, sans-serif;
    color: var(--text-white);
  }
  .canvas { position: relative; width: 1200px; height: 1000px; }

  .brushed-blue {
    background: linear-gradient(90deg,
      var(--blue-mid) 0%,
      var(--blue-light) 6%,
      var(--blue-deep) 14%,
      var(--blue-mid) 26%,
      var(--blue-light) 34%,
      var(--blue-deep) 42%,
      var(--blue-mid) 52%,
      var(--blue-light) 60%,
      var(--blue-deep) 70%,
      var(--blue-mid) 80%,
      var(--blue-light) 88%,
      var(--blue-deep) 96%,
      var(--blue-mid) 100%);
  }

  .card {
    position: absolute;
    left: 245px;
    width: 688px;
    height: 393px;
    overflow: hidden;
  }
  .card--back { top: 101px; background: var(--band-black); }
  .card--front { top: 531px; }

  .card__band {
    position: absolute;
    left: 0; top: 0;
    width: 100%;
    height: 197px;
  }
  .card__rule {
    position: absolute;
    left: 0; top: 196px;
    width: 100%;
    height: 2px;
    background: linear-gradient(90deg, transparent 0%, var(--rule-light) 30%, #ffffff 60%, var(--rule-light) 85%, transparent 100%);
  }

  .line { position: absolute; white-space: nowrap; line-height: 1; }

  .back-name { left: 20px; top: 21px; font-size: 38px; }
  .back-title { left: 24px; top: 63px; font-size: 30px; }

  .subjects-list { left: 405px; top: 20px; font-size: 20px; line-height: 26px; }

  .contact { left: 405px; font-size: 20px; }
  .contact--school { top: 259px; line-height: 26px; }
  .contact--phone { top: 316px; }
  .contact--email { top: 352px; font-size: 15px; }

  .front-name {
    left: 0; width: 100%; top: 142px;
    text-align: center; font-size: 50px;
    padding-left: 4px;
  }
  .front-title {
    left: 0; width: 100%; top: 197px;
    text-align: center; font-size: 29px;
    letter-spacing: 3px;
  }
  .front-subjects {
    left: 0; width: 100%; top: 296px;
    text-align: center; font-size: 20px;
  }
</style>
</head>
<body>
<div class="canvas">

  <section class="card card--back" aria-label="Business card, details side">
    <div class="card__band brushed-blue"></div>
    <div class="card__rule"></div>
    <div class="line back-name">Glen Mabery</div>
    <div class="line back-title">Academic Coach</div>
    <div class="line subjects-list">Subjects<br>QET and BRT<br>Math, Physics, Writing</div>
    <div class="line contact contact--school">AB Pellwood University,<br>1994 Cum Laude</div>
    <div class="line contact contact--phone">Phone: 404-555-0187</div>
    <div class="line contact contact--email">glenrmabery@tutormail-example.com</div>
  </section>

  <section class="card card--front brushed-blue" aria-label="Business card, name side">
    <div class="line front-name">Glen Mabery</div>
    <div class="line front-title">Academic Coach</div>
    <div class="line front-subjects">Subjects: QET and BRT, Math, Physics, Writing</div>
  </section>

</div>
</body>
</html>
```